Plakat-Design für Veltrana
Zielgruppe
Wir sind eine 'kreative' kleine Truppe, die mit neuen Ideen versuchen wollen, auch mal andere Wege in den Projekten zu gehen.
Aufgabenstellung
Für die Motivation meiner Mitarbeiter und für meinen Empfang suche ich Plakate in der Höhe von ca. 150 cm und Breite von etwa 50 cm.
Sie sollen die weißen Wände etwas auflockern, von daher hätte ich gern die Hauptfarbe im Hintergrund. Ansonsten bitte für die Farbakzente die CD-Farben nutzen.
Grundsätzlich soll das Thema "Einfach Machen" sein. Ich möchte damit animieren Dinge und Wege auszuprobieren, ohne vorab immer scheu davor zu haben.
Gerne auch mit weiteren Textvorschlägen. Pro neuen Text, der dann auf ein Poster kommt, zahle ich einen Bonus von 40€.

```html
<!DOCTYPE html>
<html lang="de">
<head>
<meta charset="utf-8">
<title>Veltrana – Einfach machen</title>
<link href="https://fonts.googleapis.com/css2?family=Barlow:wght@400;500;600&display=swap" rel="stylesheet">
<style>
  :root {
    --poster-bg: #434b4e;
    --accent-pink: #ef6577;
    --text-grey: #c4c4c6;
    --logo-grey: #dde1e3;
  }
  html, body {
    margin: 0;
    padding: 0;
    width: 1200px;
    height: 3598px;
    overflow: hidden;
    background: var(--poster-bg);
  }
  .poster {
    position: relative;
    width: 1200px;
    height: 3598px;
    background: var(--poster-bg);
    font-family: "Barlow", "DIN Alternate", Arial, sans-serif;
    text-align: center;
  }
  .headline {
    position: absolute;
    top: 870px;
    left: 0;
    width: 1200px;
    margin: 0;
    font-size: 290px;
    line-height: 286px;
    font-weight: 600;
    letter-spacing: 0.1em;
    text-indent: 0.1em;
    color: var(--accent-pink);
  }
  .headline span { display: block; }
  .claim {
    position: absolute;
    top: 1498px;
    left: 0;
    width: 1200px;
    margin: 0;
    font-size: 88px;
    line-height: 112px;
    font-weight: 500;
    color: var(--text-grey);
  }
  .claim span { display: block; }
  .tagline {
    position: absolute;
    top: 3145px;
    left: 0;
    width: 1200px;
    margin: 0;
    font-size: 62px;
    line-height: 62px;
    font-weight: 400;
    color: var(--text-grey);
  }
  .brand-name {
    position: absolute;
    top: 3276px;
    left: 0;
    width: 1200px;
    margin: 0;
    font-size: 160px;
    line-height: 160px;
    font-weight: 400;
    color: var(--logo-grey);
  }
</style>
</head>
<body>
  <main class="poster">
    <h1 class="headline"><span>ENFCH</span><span>MCHN</span></h1>
    <p class="claim">
      <span>DU BIST EIN GENIE,</span>
      <span>WENN DU DINGE</span>
      <span>AUF DAS WESENTLICHE</span>
      <span>REDUZIEREN KANNST.</span>
    </p>
    <p class="tagline">EINFACH MACHEN!</p>
    <p class="brand-name">Veltrana</p>
  </main>
</body>
</html>
```